This is for a poster that will be hanging in the window of a Men's Suit Store in the mall:
Size 4 feet wide by 6 feet high
Main point is: A sale on "Suits" or "Men's Suits" at 40%-60% off ( the 40%-60% off should be the focal point)
Some words that can be used are "Sale" or "Clearance Sale"
Some key words that can be used to make it urgent are "limited time offer" or something similar.
You can get creative, the point is for the customer to want to come into the store and buy a suit right away.
You may use a graphic (picture of a man in a suit). It is not necessary but if it looks good you can use it. (If you do use a picture, it should be of a modern fit or slim fit suit)
Sorry, the initial brief somehow got deleted from the project. Please see the updated brief.
Thanks
Reason: Project was closed for some reason, extended to give enough time to complete
Target Market(s)
Mostly Men ages 35-55
Industry/Entity Type
Store
Colors
Designer to choose colors to be used in the design.

```html
<!DOCTYPE html>
<html lang="en">
<head>
<meta charset="UTF-8">
<title>Men's Suits Clearance Sale Poster</title>
<link rel="stylesheet" href="https://fonts.googleapis.com/css2?family=Poiret+One&display=swap">
<style>
  :root {
    --page-bg: #e4e4e4;
    --poster-border: #ffffff;
    --photo-light: #b9b9b9;
    --photo-mid: #a3a3a3;
    --photo-dark: #3c3c3c;
    --photo-deep: #262626;
    --band: rgba(80, 80, 80, 0.42);
    --text-light: #ffffff;
    --text-brand: #2f2f2f;
  }
  * { box-sizing: border-box; margin: 0; padding: 0; }
  html, body {
    width: 1200px;
    height: 1000px;
    overflow: hidden;
    background: var(--page-bg);
  }
  .poster {
    position: absolute;
    left: 260px;
    top: 20px;
    width: 680px;
    height: 960px;
    border: 5px solid var(--poster-border);
    overflow: hidden;
    font-family: "Poiret One", "Josefin Sans", sans-serif;
    color: var(--text-light);
  }
  .poster__photo {
    position: absolute;
    inset: 0;
    background: linear-gradient(90deg,
      var(--photo-light) 0%,
      var(--photo-mid) 48%,
      var(--photo-dark) 62%,
      var(--photo-deep) 80%,
      var(--photo-dark) 100%);
  }
  .poster__category {
    position: absolute;
    top: 34px;
    left: 0;
    width: 100%;
    text-align: center;
    font-size: 40px;
    letter-spacing: 1px;
  }
  .poster__headline {
    position: absolute;
    left: 15px;
    top: 200px;
    font-weight: 400;
    line-height: 1;
  }
  .poster__headline-top {
    display: block;
    font-size: 82px;
    letter-spacing: 1px;
  }
  .poster__headline-main {
    display: block;
    font-size: 106px;
    margin-top: -6px;
  }
  .poster__discount-band {
    position: absolute;
    left: 0;
    top: 408px;
    width: 100%;
    height: 161px;
    background: var(--band);
    display: flex;
    align-items: center;
    justify-content: center;
  }
  .poster__discount {
    font-size: 100px;
    letter-spacing: 1px;
    white-space: nowrap;
  }
  .poster__urgency {
    position: absolute;
    left: 18px;
    top: 618px;
    font-size: 62px;
    line-height: 64px;
    letter-spacing: 1px;
  }
  .poster__brand {
    position: absolute;
    left: 0;
    bottom: 6px;
    width: 100%;
    text-align: center;
    color: var(--text-brand);
    line-height: 1;
  }
  .poster__brand-name { display: block; font-size: 48px; }
  .poster__brand-type { display: block; font-size: 25px; }
</style>
</head>
<body>
  <div class="poster">
    <div class="poster__photo" role="img" aria-label="Softly blurred photograph of a man in a slim-fit dark suit and tie buttoning his jacket, against a light grey studio backdrop"></div>
    <p class="poster__category">Men's Suits</p>
    <h1 class="poster__headline">
      <span class="poster__headline-top">CLERANCE</span>
      <span class="poster__headline-main">SALE!</span>
    </h1>
    <div class="poster__discount-band">
      <p class="poster__discount">40%-60% off</p>
    </div>
    <p class="poster__urgency">HURRY!<br>LIMITED TIME<br>OFFER ONLY!</p>
    <p class="poster__brand">
      <span class="poster__brand-name">marlow</span>
      <span class="poster__brand-type">menswear</span>
    </p>
  </div>
</body>
</html>
```